Creation of a cover for a novel on immigration in Paris, with one of the two joined images. These photos can be modified (shape, colors…)
Size: 14 x 20.5 cm (vertical) with 5 mm bleed on the top, bottom and right areas.

TITLE: "Teodor, the Wanderer" (and not "African immigrant in Paris)
AUTHOR: “Lucien Marvaud”
NOTICES TO BE ADDED:
- “Novel” (witch means novel)
- “Preface by Solenne Varek” (the preface writer)
PUBLISH “Editions Pluvane” (AT THE BOTTOM OF THE PAGE)

Target Market(s)

Book shops

Industry/Entity Type

Book cover

Requirements
Must have
• One of the two images joined

```html
<!DOCTYPE html>
<html lang="fr">
<head>
<meta charset="utf-8">
<title>Teodor, the Wanderer — Book Cover</title>
<link href="https://fonts.googleapis.com/css2?family=Arimo:wght@400;700&family=Bungee&display=swap" rel="stylesheet">
<style>
  :root {
    --backdrop: #6f98a8;
    --ink-white: #ffffff;
    --title-peach: #f2bf98;
    --spine-dark: #15191e;
    --night: #0e1620;
    --lamp-orange: #c8652a;
    --glow-amber: #e89a4a;
    --mist-teal: #3f7f90;
    --steel-blue: #1e3442;
  }
  * { margin: 0; padding: 0; box-sizing: border-box; }
  html, body { width: 1200px; height: 1000px; overflow: hidden; }
  body {
    background: var(--backdrop);
    font-family: "Arimo", Arial, sans-serif;
    color: var(--ink-white);
    position: relative;
  }
  .book-wrap {
    position: absolute;
    left: 68px; top: 88px;
    width: 1100px; height: 774px;
    display: flex;
  }
  .front-cover, .back-cover {
    position: relative;
    width: 510px; height: 100%;
    overflow: hidden;
  }
  .spine {
    position: relative;
    width: 80px; height: 100%;
    background: var(--spine-dark);
  }
  .cover-photo {
    position: absolute; inset: 0;
    background:
      linear-gradient(180deg, var(--night) 0%, rgba(14,22,32,0.55) 28%, rgba(14,22,32,0) 50%, rgba(14,22,32,0.35) 100%),
      linear-gradient(90deg, var(--lamp-orange) 0%, var(--glow-amber) 30%, #6a6a62 52%, var(--mist-teal) 75%, var(--steel-blue) 100%);
  }
  .back-cover .cover-photo {
    background:
      linear-gradient(180deg, var(--night) 0%, rgba(14,22,32,0.6) 20%, rgba(14,22,32,0.1) 55%, rgba(14,22,32,0.45) 100%),
      linear-gradient(90deg, var(--lamp-orange) 0%, var(--glow-amber) 35%, #5d7f84 60%, var(--mist-teal) 80%, var(--steel-blue) 100%);
  }
  .genre-label {
    position: absolute; top: 35px; left: 0; width: 100%;
    text-align: center; font-size: 14px;
  }
  .title-main {
    position: absolute; left: 0; width: 100%;
    text-align: center;
    font-family: "Bungee", "Arimo", sans-serif;
    color: var(--title-peach);
    letter-spacing: 2px;
    line-height: 1;
  }
  .title-sub {
    position: absolute; left: 0; width: 100%;
    text-align: center; color: var(--ink-white);
    letter-spacing: 0.5px;
  }
  .front-cover .title-main { top: 80px; font-size: 78px; }
  .front-cover .title-sub { top: 190px; font-size: 28px; }
  .author-name {
    position: absolute; bottom: 28px; left: 0; width: 100%;
    text-align: center; font-size: 22px;
  }
  .spine-author {
    position: absolute; left: 50%; top: 70px;
    transform: translateX(-50%) rotate(90deg);
    transform-origin: center;
    white-space: nowrap; font-size: 14px;
    width: 0; display: flex; justify-content: center;
  }
  .spine-title {
    position: absolute; left: 50%; top: 650px;
    transform: translate(-50%, -50%) rotate(90deg);
    white-space: nowrap; text-align: center; line-height: 1;
  }
  .spine-title .title-main-s {
    font-family: "Bungee", "Arimo", sans-serif;
    color: var(--title-peach); font-size: 34px; display: block;
  }
  .spine-title .title-sub-s { font-size: 14px; display: block; margin-top: 2px; }
  .about-heading {
    position: absolute; top: 98px; left: 0; width: 100%;
    text-align: center; font-size: 15px; font-weight: 700;
  }
  .about-text {
    position: absolute; top: 136px; left: 42px; right: 42px;
    text-align: center; font-size: 14px; font-weight: 700; line-height: 18px;
  }
  .back-cover .title-main { top: 562px; font-size: 66px; }
  .back-cover .title-sub { top: 660px; font-size: 24px; }
  .preface-line {
    position: absolute; top: 712px; left: 0; width: 100%;
    text-align: center; font-size: 14px; font-weight: 700;
  }
  .publisher-line {
    position: absolute; top: 734px; left: 0; width: 100%;
    text-align: center; font-size: 14px; font-weight: 700;
  }
</style>
</head>
<body>
  <main class="book-wrap">
    <section class="front-cover">
      <div class="cover-photo" role="img" aria-label="Night train station platform with a traveller carrying a backpack and bag, seen from behind, orange lamplight on the left and misty teal light on the right"></div>
      <p class="genre-label">Roman</p>
      <h1 class="title-main">TEODOR</h1>
      <p class="title-sub">THE WANDERER</p>
      <p class="author-name">Lucien Marvaud</p>
    </section>

    <aside class="spine">
      <p class="spine-author"><span>Lucien Marvaud</span></p>
      <p class="spine-title"><span class="title-main-s">TEODOR</span><span class="title-sub-s">THE WANDERER</span></p>
    </aside>

    <section class="back-cover">
      <div class="cover-photo" role="img" aria-label="Foggy night train station platform with lit carriages and distant figures, orange glow blending into teal mist"></div>
      <h2 class="about-heading">About The Author</h2>
      <p class="about-text">Lorem ipsum dolor sit amet, consectetur adipiscing elit, sed do eiusmod tempor incididunt ut labore et dolore magna aliqua. Quis ipsum suspendisse ultrices gravida. Risus commodo viverra maecenas accumsan lacus vel facilisis. Lorem ipsum dolor sit amet, consectetur adipiscing elit, sed do eiusmod tempor incididunt ut labore et dolore magna aliqua. Quis ipsum suspendisse ultrices gravida. Risus commodo viverra maecenas accumsan lacus vel facilisis.<br>Lorem ipsum dolor sit amet, consectetur adipiscing elit, sed do eiusmod tempor incididunt ut labore et dolore magna aliqua. Quis ipsum suspendisse ultrices gravida. Risus commodo viverra maecenas accumsan lacus vel facilisis.</p>
      <p class="title-main">TEODOR</p>
      <p class="title-sub">THE WANDERER</p>
      <p class="preface-line">Préface de Solenne Varek</p>
      <p class="publisher-line">PUBLISHER "Editions Pluvane"</p>
    </section>
  </main>
</body>
</html>
```